Stroomwacht Powerpoint - presentation slides for energy management tool

We need a Powerpoint presentation lay-out which matches our logo from Stroomwacht.nl. 10 slides variations minimum, enough for a full professional presentation to potential clients.
Stroomwacht is a Dutch energymanagement tool for corporate real estate and housing agency. Our clients are Social houseing organisation, real estate owers, property managers and property developers.
Target Market(s)
real estate owners
Property manage
Font styles to use
Sans Serif
Colors
f78f20
0255a3
Requirements
Must have
- Stroomwacht logo colors and style
#F37122 orange
#00345D darkblue
Nice to have
- Professional look, background not white in every slide
Should not have
- wrong color orange and blue.

```html
<!DOCTYPE html>
<html lang="en">
<head>
<meta charset="utf-8">
<title>Stroomwacht – Presentation Slides</title>
<link href="https://fonts.googleapis.com/css2?family=Montserrat:wght@400;500;600;700&display=swap" rel="stylesheet">
<style>
:root{
  --navy:#00345d;
  --navy-deep:#0b2f57;
  --orange:#f37122;
  --page:#ececec;
  --ink:#1d1d1f;
  --muted:#6b6f76;
  --white:#ffffff;
}
*{box-sizing:border-box;margin:0;padding:0}
html,body{width:695px;height:1200px;overflow:hidden;background:var(--page);font-family:'Montserrat',sans-serif;color:var(--ink)}
.board{position:relative;width:695px;height:1200px}
.slide{position:absolute;width:322px;height:181px;overflow:hidden;background:var(--white);box-shadow:0 2px 5px rgba(0,0,0,.25)}
.col-l{left:19px}.col-r{left:357px}
.row1{top:21px}.row2{top:217px}.row3{top:412px}.row4{top:608px}.row5{top:804px}.row6{top:999px}
.abs{position:absolute}
.photo{position:absolute}

/* logo */
.logo{position:absolute;display:flex;align-items:center;gap:3px;font-weight:500;white-space:nowrap;letter-spacing:-.2px}
.logo .dot{border-radius:50%;background:var(--orange);flex:none}
.logo.sm{font-size:10px}.logo.sm .dot{width:9px;height:9px}
.logo.md{font-size:17px}.logo.md .dot{width:15px;height:15px}
.logo.lg{font-size:21px}.logo.lg .dot{width:18px;height:18px}
.on-dark{color:var(--white)}.on-light{color:var(--navy)}

/* titles */
.title{position:absolute;left:10px;top:8px;font-size:12.5px;font-weight:700;color:var(--ink);letter-spacing:-.2px}
.title::after{content:"";display:block;width:14px;height:1.5px;background:var(--navy);margin-top:4px}
.kicker{font-size:4.3px;font-weight:700;letter-spacing:2px;color:var(--navy)}
.body{font-size:3.6px;line-height:9.6px;color:#333;text-align:justify}
.small{font-size:3.6px;line-height:4.8px;color:var(--muted);text-align:center}

/* footer band */
.footer{position:absolute;left:0;right:0;bottom:0;height:6px;background:linear-gradient(110deg,var(--navy) 53%,var(--orange) 53.4%)}
.footer span{position:absolute;left:6px;top:1px;font-size:2.8px;color:var(--white)}
.footer b{position:absolute;right:4px;top:1px;font-size:3px;color:var(--white);font-weight:500}

.frame{position:absolute;left:5px;top:5px;right:5px;bottom:5px;border:1px solid rgba(255,255,255,.85)}

/* about stats */
.stats{position:absolute;left:186px;top:45px;width:136px;height:96px;background:var(--navy);padding:6px 8px}
.stat{display:flex;align-items:center;height:28px;color:var(--white)}
.stat svg{width:12px;height:12px;flex:none}
.stat i{width:1px;height:18px;background:var(--white);margin:0 7px}
.stat strong{font-size:13px;font-weight:600;width:40px}
.stat small{font-size:3.4px;line-height:4px;width:42px}

/* timeline */
.flag{position:absolute;top:62px;width:45px;height:10px;color:var(--white);font-size:7.5px;font-weight:700;text-align:center;line-height:10px;clip-path:polygon(4px 0,100% 0,calc(100% - 4px) 100%,0 100%)}
.flag.n{background:var(--navy)}.flag.o{background:var(--orange)}
.stem{position:absolute;top:72px;width:1px;height:28px}
.tbox{position:absolute;top:100px;width:43px;height:53px;background:var(--white);box-shadow:0 1px 3px rgba(0,0,0,.2);text-align:center;padding-top:12px}
.tbox h4{font-size:4px;letter-spacing:1px;font-weight:700;margin-bottom:4px}
.tbox p{font-size:3.4px;line-height:4.6px;color:var(--muted);padding:0 3px}

/* projects */
.card{position:absolute;top:61px;width:94px;height:112px;border:1px dashed #8a8f97}
.card .pic{position:absolute;left:4px;top:10px;right:4px;height:60px}
.card h4{position:absolute;top:80px;width:100%;text-align:center;font-size:4.3px;letter-spacing:1.3px;color:var(--navy);font-weight:700}
.card p{position:absolute;top:91px;width:100%;padding:0 8px}
.num{position:absolute;top:42px;width:25px;height:25px;background:var(--white);color:var(--navy);font-size:12px;font-weight:700;text-align:center;line-height:25px;box-shadow:0 1px 2px rgba(0,0,0,.2)}

/* team */
.member{position:absolute;top:53px;width:90px;text-align:center}
.member .pic{width:53px;height:53px;border-radius:50%;margin:0 auto 7px}
.member h5{font-size:5px;font-weight:700;color:var(--navy)}
.member h6{font-size:4px;letter-spacing:1px;font-weight:700;color:var(--navy);margin:1px 0 8px}

/* contact */
.contact{position:absolute;left:25px;top:108px;color:var(--white);font-size:4.6px;line-height:5.6px}
.contact li{list-style:none;display:flex;gap:7px;align-items:flex-start;margin-bottom:8px}
.contact svg{width:8px;height:8px;flex:none}
</style>
</head>
<body>
<main class="board">

<!-- 1 brand cover -->
<section class="slide col-l row1" style="background:var(--navy)">
  <div class="logo lg on-dark" style="left:105px;top:78px"><span class="dot"></span>Stroomwacht</div>
</section>

<!-- 2 photo cover -->
<section class="slide col-r row1">
  <div class="photo" role="img" aria-label="Suburban house at dusk" style="inset:0;background:linear-gradient(180deg,#6c6f86 0%,#8f7d86 25%,#39465c 60%,#2a3040 100%)"></div>
  <div class="frame"></div>
  <div class="logo lg on-dark" style="left:78px;top:78px"><span class="dot"></span>Stroomwacht</div>
  <div class="abs" style="left:0;right:0;top:163px;text-align:center;font-size:4px;letter-spacing:2px;color:#fff">WWW.STROOMWACHT.NL</div>
</section>

<!-- 3 master light -->
<section class="slide col-l row2">
  <div class="photo" role="img" aria-label="Faded photo of a family house" style="inset:0;background:linear-gradient(180deg,#f4f4f4 0%,#e0e0e0 45%,#d0d0d0 75%,#e9e9e9 100%)"></div>
  <div class="abs" style="left:160px;top:13px;width:1.5px;height:155px;background:var(--navy)"></div>
  <div class="logo md on-light" style="left:21px;top:83px"><span class="dot"></span>Stroomwacht</div>
  <div class="abs" style="right:14px;top:15px;text-align:right;font-size:14px;font-weight:700;line-height:17px;color:var(--ink)">MASTER SLIDE<br>PRESENTATION</div>
  <div class="abs kicker" style="right:14px;top:56px">SUBTITLE GOES HERE</div>
  <div class="abs" style="right:15px;top:66px;width:20px;height:1.5px;background:var(--navy)"></div>
  <div class="abs" style="right:11px;top:161px;display:flex;gap:1.5px">
    <span style="width:7px;height:7px;border:.8px solid var(--navy);border-radius:50%"></span>
    <span style="width:7px;height:7px;border:.8px solid var(--navy);border-radius:50%"></span>
    <span style="width:7px;height:7px;border:.8px solid var(--navy);border-radius:50%"></span>
  </div>
</section>

<!-- 4 master dark -->
<section class="slide col-r row2">
  <div class="photo" role="img" aria-label="House exterior tinted navy" style="inset:0;background:linear-gradient(135deg,#1f4670 0%,#173e68 50%,#12355b 100%)"></div>
  <div class="abs" style="left:186px;top:16px;width:86px;height:86px;border-radius:50%;background:var(--orange)"></div>
  <div class="abs" style="left:12px;top:35px;font-size:13px;font-weight:700;line-height:17px;color:#fff">MASTER SLIDE<br>PRESENTATION</div>
  <div class="abs kicker" style="left:12px;top:74px;color:var(--orange)">SUBTITLE GOES HERE</div>
  <div class="abs" style="left:12px;top:83px;width:20px;height:1.5px;background:#fff"></div>
  <div class="abs" style="left:14px;top:166px;font-size:4px;letter-spacing:2px;color:#fff">WWW.STROOMWACHT.NL</div>
  <div class="abs" style="right:8px;top:166px;font-size:4.5px;font-weight:600;color:#fff">2020</div>
</section>

<!-- 5 agenda -->
<section class="slide col-l row3">
  <div class="photo" role="img" aria-label="Entrance hall with front door" style="left:0;top:0;width:154px;height:167px;background:linear-gradient(90deg,#5a5650 0%,#d9d9d6 30%,#eeeeec 60%,#8a7458 100%)"></div>
  <div class="abs" style="left:77px;top:118px;width:91px;height:31px;background:#fff;box-shadow:0 1px 3px rgba(0,0,0,.25);text-align:center;line-height:31px;font-size:12.5px;font-weight:700;color:var(--navy)">AGENDA</div>
  <div class="abs" style="left:184px;top:34px;width:78px;height:78px;border-radius:50%;background:#f1f1f1"></div>
  <ol class="abs" style="left:208px;top:49px;list-style:none;font-size:5px;font-weight:600;color:var(--navy);line-height:12.9px">
    <li>i.&nbsp; Introduction</li><li>ii.&nbsp; About Us</li><li>iii.&nbsp; Welcome Massage</li><li>iv.&nbsp; Portfolio</li><li>v.&nbsp; Our Services</li><li>vi.&nbsp; Team</li><li>vii. Company values</li><li>viii. Contact Us</li>
  </ol>
  <div class="logo sm on-light" style="right:10px;top:14px"><span class="dot"></span>Stroomwacht</div>
  <div class="footer"><span>© Stroomwacht. 2020 - All rights reserved.</span><b>| 5</b></div>
</section>

<!-- 6 about -->
<section class="slide col-r row3">
  <h2 class="title">ABOUT US</h2>
  <div class="logo sm on-light" style="right:10px;top:14px"><span class="dot"></span>Stroomwacht</div>
  <div class="abs kicker" style="left:86px;top:49px;font-size:4px">SUBTITLE GOES HERE</div>
  <p class="abs body" style="left:22px;top:60px;width:143px">Lorem ipsum dolor sit amet, consectetuer adipiscing elit, sed diam nonummy nibh euismod tincidunt ut laoreet dolore magna aliquam erat volutpat. Ut wisi enim ad minim veniam, quis nostrud exerci tation ullamcorper suscipit lobortis nisl ut aliquip ex ea commodo consequat. Duis autem vel eum iriure dolor in hendrerit in vulputate velit esse molestie consequat, vel illum dolore eu feugiat nulla facilisis at vero eros et accumsan et iusto odio dignissim qui blandit praesent luptatum zzril delenit augue duis dolore te feugait nulla facilisi. Lorem ipsum dolor sit amet</p>
  <div class="stats">
    <div class="stat"><svg viewBox="0 0 12 12" fill="none" stroke="#fff" stroke-width=".7"><path d="M1 5h10L6 2z"/><path d="M2 5v5M4.5 5v5M7.5 5v5M10 5v5M1 10.5h10"/></svg><i></i><strong>1220</strong><small>Lorem ipsum dolor sit amet, consectetuer adipiscing elit.</small></div>
    <div class="stat"><svg viewBox="0 0 12 12" fill="none" stroke="#fff" stroke-width=".7"><circle cx="3.5" cy="5" r="1.5"/><circle cx="8.5" cy="5" r="1.5"/><path d="M1 10c0-2 1-3 2.5-3S6 8 6 10M6 10c0-2 1-3 2.5-3S11 8 11 10"/></svg><i></i><strong>100</strong><small>Lorem ipsum dolor sit amet, consectetuer adipiscing elit.</small></div>
    <div class="stat"><svg viewBox="0 0 12 12" fill="none" stroke="#fff" stroke-width=".7"><circle cx="6" cy="2.5" r="1.2"/><path d="M5.4 3.6L2 11M6.6 3.6L10 11M3.5 8h5"/></svg><i></i><strong>85%</strong><small>Lorem ipsum dolor sit amet, consectetuer adipiscing elit.</small></div>
  </div>
  <div class="footer"><span>© Stroomwacht. 2020 - All rights reserved.</span><b>| 6</b></div>
</section>

<!-- 7 welcome -->
<section class="slide col-l row4">
  <h2 class="title">WELCOME <span style="color:var(--navy)">MESSAGE</span></h2>
  <div class="logo sm on-light" style="right:10px;top:14px"><span class="dot"></span>Stroomwacht</div>
  <div class="abs" style="left:16px;top:36px;width:91px;height:124px;border:1.5px solid var(--navy)"></div>
  <div class="photo" role="img" aria-label="Portrait of the director on the phone" style="left:25px;top:44px;width:91px;height:121px;background:linear-gradient(160deg,#d9dde2 0%,#a9b6c6 50%,#7d92ad 100%);box-shadow:0 1px 3px rgba(0,0,0,.25)"></div>
  <div class="abs" style="left:127px;top:44px;font-size:40px;font-weight:700;color:#c9c9c9;line-height:40px">“</div>
  <div class="abs kicker" style="right:17px;top:59px;font-size:4px">SUBTITLE GOES HERE</div>
  <p class="abs body" style="left:142px;top:71px;width:165px">Lorem ipsum dolor sit amet, consectetuer adipiscing elit, sed diam nonummy nibh euismod tincidunt ut laoreet dolore magna aliquam erat volutpat. Ut wisi enim ad minim veniam, quis nostrud exerci tation ullamcorper suscipit lobortis nisl ut aliquip ex ea commodo consequat. Duis autem vel eum iriure dolor in hendrerit in vulputate velit esse molestie consequat, vel illum dolore eu feugiat nulla facilisis at vero eros et accumsan et iusto odio dignissim qui blandit praesent luptatum zzril delenit augue duis dolore te feugait nulla facilisi. Lorem ipsum dolor sit amet</p>
  <div class="footer"><span>© Stroomwacht. 2020 - All rights reserved.</span><b>| 7</b></div>
</section>

<!-- 8 timeline -->
<section class="slide col-r row4">
  <h2 class="title">TIMELINE</h2>
  <div class="logo sm on-light" style="right:10px;top:14px"><span class="dot"></span>Stroomwacht</div>
  <div class="flag n" style="left:31px">2015</div><div class="stem" style="left:42px;background:var(--navy)"></div>
  <div class="flag o" style="left:86px">2016</div><div class="stem" style="left:97px;background:var(--orange)"></div>
  <div class="flag n" style="left:139px">2017</div><div class="stem" style="left:150px;background:var(--navy)"></div>
  <div class="flag o" style="left:193px">2018</div><div class="stem" style="left:204px;background:var(--orange)"></div>
  <div class="flag n" style="left:249px">2020</div><div class="stem" style="left:260px;background:var(--navy)"></div>
  <div class="tbox" style="left:31px"><h4 style="color:var(--navy)">YOUR TEXT</h4><p>Lorem Ipsum is simply dummy text of the printing and typesetting industry.</p></div>
  <div class="tbox" style="left:86px"><h4 style="color:var(--orange)">YOUR TEXT</h4><p>Lorem Ipsum is simply dummy text of the printing and typesetting industry.</p></div>
  <div class="tbox" style="left:139px"><h4 style="color:var(--navy)">YOUR TEXT</h4><p>Lorem Ipsum is simply dummy text of the printing and typesetting industry.</p></div>
  <div class="tbox" style="left:194px"><h4 style="color:var(--orange)">YOUR TEXT</h4><p>Lorem Ipsum is simply dummy text of the printing and typesetting industry.</p></div>
  <div class="tbox" style="left:250px"><h4 style="color:var(--navy)">YOUR TEXT</h4><p>Lorem Ipsum is simply dummy text of the printing and typesetting industry.</p></div>
  <div class="footer"><span>© Stroomwacht. 2020 - All rights reserved.</span><b>| 8</b></div>
</section>

<!-- 9 projects -->
<section class="slide col-l row5">
  <div class="photo" role="img" aria-label="Modern building facade tinted navy" style="left:0;top:0;right:0;height:55px;background:linear-gradient(90deg,#1e4a78 0%,#2b5685 50%,#1e4a78 100%)"></div>
  <div class="abs" style="left:0;right:0;top:9px;text-align:center;font-size:12.5px;font-weight:700;color:#fff">OUR PROJECTS</div>
  <div class="abs" style="left:152px;top:27px;width:20px;height:1.5px;background:#fff"></div>
  <div class="card" style="left:11px"><div class="pic" role="img" aria-label="Blue family house at dusk" style="background:linear-gradient(180deg,#c7a2c6 0%,#5d6b91 55%,#434d5f 100%)"></div><h4>ADD YOUR TITLE HERE</h4><p class="small">Lorem Ipsum is simply dummy text of the printing and typesetting industry.</p></div>
  <div class="card" style="left:113px"><div class="pic" role="img" aria-label="Brown bungalow with lawn" style="background:linear-gradient(180deg,#6f94b8 0%,#8a6d48 50%,#5e7e3c 80%,#b6bcc0 100%)"></div><h4>ADD YOUR TITLE HERE</h4><p class="small">Lorem Ipsum is simply dummy text of the printing and typesetting industry.</p></div>
  <div class="card" style="left:214px"><div class="pic" role="img" aria-label="Modern two-storey house" style="background:linear-gradient(180deg,#9fb6c9 0%,#4b5e79 50%,#5d5245 80%,#a9a39b 100%)"></div><h4>ADD YOUR TITLE HERE</h4><p class="small">Lorem Ipsum is simply dummy text of the printing and typesetting industry.</p></div>
  <div class="num" style="left:19px">01</div><div class="num" style="left:120px">02</div><div class="num" style="left:221px">03</div>
  <div class="footer"><span>© Stroomwacht. 2020 - All rights reserved.</span><b>| 9</b></div>
</section>

<!-- 10 section -->
<section class="slide col-r row5">
  <div class="photo" role="img" aria-label="Living room interior tinted navy" style="inset:0;background:linear-gradient(180deg,#4b6585 0%,#345276 50%,#29476c 100%)"></div>
  <div class="abs" style="left:0;right:0;top:52px;height:78px;background:rgba(14,52,95,.85)"></div>
  <div class="frame"></div>
  <div class="logo md on-dark" style="left:15px;top:82px"><span class="dot"></span>Stroomwacht</div>
  <div class="abs" style="left:117px;top:58px;width:1px;height:66px;background:#fff"></div>
  <div class="abs" style="left:128px;top:70px;display:flex;align-items:baseline;gap:6px;color:#fff"><span style="font-size:17px;font-weight:700">01</span><span style="font-size:4.8px;letter-spacing:1.3px;font-weight:700">ADD YOUR TITLE TEXT HERE</span></div>
  <p class="abs" style="left:129px;top:94px;width:180px;font-size:3.6px;line-height:9.5px;color:#fff">Lorem ipsum dolor sit amet, consectetuer adipiscing elit, sed diam nonummy nibh euismod tincidunt ut laoreet dolore magna aliquam erat volutpat.</p>
</section>

<!-- 11 team -->
<section class="slide col-l row6">
  <h2 class="title">OUR TEAM</h2>
  <div class="logo sm on-light" style="right:10px;top:14px"><span class="dot"></span>Stroomwacht</div>
  <div class="member" style="left:25px"><div class="pic" role="img" aria-label="Team member portrait" style="background:radial-gradient(circle,#9a9a9a,#505050)"></div><h5>NAME</h5><h6>POTITION/CEO</h6><p class="small" style="line-height:7.3px">Lorem ipsum dolor sit amet, consectetuer adipiscing elit, sed diam nonummy nibh</p></div>
  <div class="member" style="left:117px"><div class="pic" role="img" aria-label="Team member portrait" style="background:radial-gradient(circle,#8a8a8a,#3e3e3e)"></div><h5>NAME</h5><h6>POTITION</h6><p class="small" style="line-height:7.3px">Lorem ipsum dolor sit amet, consectetuer adipiscing elit, sed diam nonummy nibh</p></div>
  <div class="member" style="left:209px"><div class="pic" role="img" aria-label="Team member portrait" style="background:radial-gradient(circle,#e4e4e4,#b7b7b7)"></div><h5>NAME</h5><h6>POTITION</h6><p class="small" style="line-height:7.3px">Lorem ipsum dolor sit amet, consectetuer adipiscing elit, sed diam nonummy nibh</p></div>
  <div class="footer"><span>© Stroomwacht. 2020 - All rights reserved.</span><b>| 11</b></div>
</section>

<!-- 12 thank you -->
<section class="slide col-r row6">
  <div class="abs" style="left:35px;top:32px;font-size:12.5px;font-weight:700;color:var(--ink)">THANK YOU</div>
  <div class="abs" style="left:36px;top:49px;width:20px;height:1.5px;background:var(--navy)"></div>
  <div class="logo md on-light" style="right:20px;top:32px"><span class="dot"></span>Stroomwacht</div>
  <div class="photo" role="img" aria-label="Patio and garden tinted navy" style="left:0;right:0;top:80px;bottom:0;background:linear-gradient(90deg,#2a4e78 0%,#3a5d84 55%,#274a72 100%)"></div>
  <ul class="contact">
    <li><svg viewBox="0 0 8 8" fill="#fff"><path d="M1.6.5l1.3 1.6-.7.9c.5 1.1 1.3 1.9 2.4 2.4l.9-.7L7.1 6 6.4 7.3C3.4 7 1 4.6.6 1.5z"/></svg>(123) 456-7890</li>
    <li><svg viewBox="0 0 8 8" fill="none" stroke="#fff" stroke-width=".6"><circle cx="4" cy="4" r="3.3"/><path d="M.7 4h6.6M4 .7c-1.8 2-1.8 4.6 0 6.6M4 .7c1.8 2 1.8 4.6 0 6.6"/></svg>www.stroomwacht.nl</li>
    <li><svg viewBox="0 0 8 8" fill="#fff"><path d="M.5 1.5h7v5h-7z"/><path d="M.5 1.5L4 4.3l3.5-2.8" stroke="#2a4e78" stroke-width=".6" fill="none"/></svg>info@stroomwacht.nl</li>
    <li><svg viewBox="0 0 8 8" fill="#fff"><path d="M4 .4a2.6 2.6 0 0 0-2.6 2.6C1.4 5 4 7.6 4 7.6S6.6 5 6.6 3A2.6 2.6 0 0 0 4 .4zm0 3.6a1 1 0 1 1 0-2 1 1 0 0 1 0 2z"/></svg><span>Stroomwacht<br>Havenstraat 12<br>1000 AB Amsterdam</span></li>
  </ul>
</section>

</main>
</body>
</html>
```